High School Senior Ad for annual

My son is a senior, and we bought an Ad for the back of the annual and looking for a one page Ad that meets the below specification. We have to submit out final Ad by Monday 11/07/22.

Specifications:
- Must be a JPEG @ 300 DPI.
- Full page size is 8.667 inches wide by 11.333 inches tall, or 2600 pixels by 3400 pixels.
- Do NOT take wording to the edge. Leave at least ½ inch on all sides without wording.

What we want:
- Looking for a creative artistic use of the photo we provide
- His name Tobin Hale should be in a very artistic script at the top
- Insert the attached bible verse and text somewhere on the Ad
- I'm attaching some examples of some that we like along with the photos that we want to use. Please look at the instruction doc to understand what we are looking for.
- If you have questions, please ask

```html
<!DOCTYPE html>
<html lang="en">
<head>
<meta charset="utf-8">
<title>Tobin Hale – Senior Ad</title>
<link href="https://fonts.googleapis.com/css2?family=Kaushan+Script&family=Montserrat:wght@400;500;700&display=swap" rel="stylesheet">
<style>
  :root {
    --backdrop: #ffffff;
    --pink: #e8609f;
    --pink-soft: #ee86b6;
    --navy: #0d2a57;
    --navy-deep: #0a2148;
    --blue-haze: #1d4a93;
    --white: #ffffff;
    --ink-light: #f2f4fa;
  }
  html, body {
    margin: 0;
    padding: 0;
    width: 1200px;
    height: 2830px;
    overflow: hidden;
    background: var(--backdrop);
  }
  .canvas {
    position: relative;
    width: 1200px;
    height: 2830px;
  }
  .ad-page {
    position: absolute;
    left: 50px;
    top: 701px;
    width: 882px;
    height: 1144px;
    transform: scale(1.2472);
    transform-origin: top left;
    overflow: hidden;
    background:
      radial-gradient(ellipse 260px 380px at 470px 520px, rgba(40,90,170,.55), transparent 70%),
      radial-gradient(ellipse 220px 260px at 700px 360px, rgba(30,75,150,.45), transparent 70%),
      var(--navy);
    box-shadow: 0 12px 30px rgba(0,0,0,.35);
    font-family: "Montserrat", sans-serif;
  }
  .pink-column {
    position: absolute;
    left: 0; top: 0;
    width: 362px; height: 1144px;
    background: linear-gradient(180deg, var(--pink) 0%, var(--pink-soft) 60%, #d6589a 100%);
  }
  .photo {
    position: absolute;
  }
  .photo--portrait {
    left: 0; top: 0;
    width: 430px; height: 882px;
    background:
      radial-gradient(ellipse 170px 420px at 215px 500px, rgba(20,40,90,.9), rgba(20,40,90,0) 80%),
      linear-gradient(180deg, #e9b58f 0%, #b7c6e8 30%, #1b2f66 55%, #cbb795 85%, #cbb795 100%);
    opacity: .92;
  }
  .photo--wall { left: 451px; top: 645px; width: 388px; height: 225px;
    background: linear-gradient(180deg, #d63a3a 0%, #e8dede 30%, #c93636 55%, #8a4a3a 80%, #3a3a3e 100%); }
  .photo--golf { left: 46px; top: 883px; width: 388px; height: 225px;
    background: linear-gradient(180deg, #c9d2cf 0%, #4a5a3a 45%, #6f8f3f 80%, #4d6b2e 100%); }
  .photo--steps { left: 451px; top: 883px; width: 388px; height: 225px;
    background: linear-gradient(120deg, #3a3a3a 0%, #e7ddd0 35%, #a9bde0 65%, #8e8d8a 100%); }

  .title-box {
    position: absolute;
    left: 380px; top: 15px;
    width: 502px; height: 103px;
    background: var(--white);
    border-bottom: 6px solid var(--navy-deep);
    box-sizing: border-box;
    display: flex; align-items: center; justify-content: center;
  }
  .student-name {
    margin: 0;
    font-family: "Kaushan Script", cursive;
    font-weight: 400;
    font-size: 66px;
    color: var(--pink);
    line-height: 1;
    padding-bottom: 6px;
  }
  .verse-box {
    position: absolute;
    left: 435px; top: 128px;
    width: 447px; height: 75px;
    background: var(--white);
    padding: 7px 0 0 21px;
    box-sizing: border-box;
  }
  .verse {
    margin: 0;
    font-weight: 700;
    font-size: 17.5px;
    line-height: 23px;
    color: var(--pink);
    text-transform: uppercase;
  }
  .message {
    position: absolute;
    left: 454px;
    width: 390px;
    color: var(--ink-light);
    font-size: 12.4px;
    line-height: 15.6px;
    margin: 0;
  }
  .message--parents { top: 224px; }
  .heading {
    position: absolute;
    margin: 0;
    font-weight: 700;
    font-size: 15.5px;
    color: var(--pink);
  }
  .heading--remember { left: 454px; top: 407px; }
  .heading--brother { left: 458px; top: 530px; }
  .quote-mark {
    position: absolute;
    font-weight: 700;
    font-size: 22px;
    color: var(--pink);
    line-height: 1;
  }
  .quote-mark--open { left: 455px; top: 437px; }
  .quote-mark--close { left: 546px; top: 473px; }
  .quote-text {
    position: absolute;
    left: 478px; top: 440px;
    width: 350px;
    margin: 0;
    color: var(--ink-light);
    font-size: 12.4px;
    line-height: 15.6px;
  }
  .quote-credit {
    position: absolute;
    right: 64px; top: 483px;
    margin: 0;
    font-weight: 700;
    font-size: 15.5px;
    color: var(--pink);
  }
  .signature {
    position: absolute;
    margin: 0;
    font-weight: 700;
    font-size: 15.5px;
  }
  .signature--parents { left: 671px; top: 505px; color: var(--white); }
  .signature--brother { left: 673px; top: 602px; color: var(--pink); }
  .message--brother { top: 559px; width: 340px; left: 457px; }
</style>
</head>
<body>
<div class="canvas">
  <article class="ad-page">
    <div class="pink-column"></div>
    <div class="photo photo--portrait" role="img" aria-label="Senior portrait of Tobin in navy blazer, light blue shirt and striped tie, leaning against a wall"></div>

    <header class="title-box">
      <h1 class="student-name">Tobin Hale</h1>
    </header>
    <div class="verse-box">
      <p class="verse">Behold, children are a gift<br>from the Lord....<br>Psalm 127:3</p>
    </div>

    <p class="message message--parents">Tobin, you are a blessing from the Lord, and we are so thankful for you.&nbsp; You have brought so much joy and love into our lives.&nbsp; It has been an honor to watch you grow into an amazing, kind, intelligent, and hard-working young man. We have loved every minute of watching you play golf for BCS.&nbsp; Your strong work ethic during golf season was inspiring.&nbsp; We are so proud of you, and we are excited to see the wonderful plans God has for your life.&nbsp; We will a lways be here to love, support, and encourage you.&nbsp; We hope you never outgrow your love of travel, history, and a good book!</p>

    <h2 class="heading heading--remember">Remember,</h2>
    <span class="quote-mark quote-mark--open">&ldquo;</span>
    <p class="quote-text">The more that you read, the more things that you will know.&nbsp; The more that you learn, the more places you'll go!</p>
    <span class="quote-mark quote-mark--close">&rdquo;</span>
    <p class="quote-credit">– Dr. Wendell Love,</p>
    <p class="signature signature--parents">Mom &amp; Dad</p>

    <h2 class="heading heading--brother">Tobin,</h2>
    <p class="message message--brother">Congrats on graduating!&nbsp; I hope you enjoyed your senior year as much as I did.&nbsp; Good luck at Ridgewood; you'll do great!</p>
    <p class="signature signature--brother">Love, Caleb</p>

    <div class="photo photo--wall" role="img" aria-label="Tobin in sunglasses standing by a dark SUV in front of a red and white striped painted brick wall"></div>
    <div class="photo photo--golf" role="img" aria-label="Tobin carrying a golf bag across a golf course beside a brick silo"></div>
    <div class="photo photo--steps" role="img" aria-label="Tobin seated on outdoor steps beside an iron railing"></div>
  </article>
</div>
</body>
</html>
```